IT Services company general flyer

Looking for a printable US letter size flyer to give a brief overview of the services we offer. We also partner with another company for their services as well. Please check out our website at www.gearbymarlon.com and click on "Our Services" to learn about our services and visit www.bluepinesafety,com and click on services to learn about their services. Several of our services do overlap, so they only need to be on the flyer once. Let me know if this is too much content and we need to weed some out. We do not want Home phone service on this flyer. The basic design of the flyer should mimic similar to the VOIP one you did for me for the colors and logo. Also check out the "Who Choose us" page on www.gearbymarlon.com to include some of that as well.
Updates

Gathering more feedback

Target Market(s)

Targeting Small businesses that may not normally have a budget for their IT Services

Industry/Entity Type

It Service

Font styles to use
Serif
Sans Serif

Requirements
Must have
• Must include my logo, phone number and email/website address and must follow the same basic template of my previous flyers.

```html
<!DOCTYPE html>
<html lang="en">
<head>
<meta charset="utf-8">
<title>Gear By Marlon – IT Services Flyer</title>
<link rel="stylesheet" href="https://fonts.googleapis.com/css2?family=Open+Sans:wght@300;400;600;700;800&display=swap">
<style>
:root{
  --red:#b3262b;
  --red-deep:#8c1a1f;
  --navy:#15305e;
  --text:#4a4a4a;
  --black:#111;
  --rule:#9a9a9a;
  --white:#fff;
}
*{margin:0;padding:0;box-sizing:border-box}
html,body{width:969px;height:1200px;overflow:hidden;background:var(--white)}
body{font-family:"Open Sans",Arial,sans-serif;position:relative}
.flyer{position:absolute;inset:0;width:969px;height:1200px;overflow:hidden;background:var(--white)}
.hero-photo{position:absolute;left:0;top:0;width:969px;height:530px;
  background:
    radial-gradient(circle at 58% 52%,rgba(255,200,215,.9) 0,rgba(240,190,210,.5) 16%,rgba(200,215,240,0) 40%),
    linear-gradient(90deg,#b9d1ec 0%,#cfd9ec 45%,#e9d7e2 58%,#3a3d48 70%,#141519 80%,#0f1013 100%);}
.hero-shapes{position:absolute;left:0;top:0;width:969px;height:580px}
.brand{position:absolute;left:52px;top:418px;display:flex;align-items:center;gap:16px}
.brand-mark{width:58px;height:58px;border-radius:50%;background:var(--red)}
.brand-name{font-weight:800;color:var(--navy);font-size:38px;line-height:1;letter-spacing:-.5px}
.services-pill{position:absolute;left:588px;top:498px;width:270px;height:54px;border-radius:12px;
  background:var(--red);color:var(--white);font-weight:600;font-size:30px;
  display:flex;align-items:center;justify-content:center}

.why-title{position:absolute;left:46px;top:562px;width:360px;color:var(--red);font-weight:700;font-size:35px;line-height:43px}
.why-head{position:absolute;left:46px;width:350px;color:var(--black);font-weight:600;font-size:21px;line-height:25px}
.why-text{position:absolute;left:46px;width:352px;color:var(--text);font-weight:400;font-size:12.6px;line-height:16.6px;text-align:justify}

.divider{position:absolute;left:418px;top:662px;width:1px;height:390px;background:#e2e2e2}
.offer{position:absolute;left:445px;top:568px;width:500px;color:var(--red);font-weight:700;font-size:18px;line-height:23px}

.service{position:absolute;left:444px;width:515px;display:flex;align-items:flex-start;gap:18px}
.service-icon{flex:none;width:66px;height:66px;border-radius:50%;background:var(--red);display:flex;align-items:center;justify-content:center}
.service-icon svg{width:36px;height:36px}
.service h3{color:var(--navy);font-weight:700;font-size:22px;line-height:26px;white-space:nowrap}
.service p{color:var(--text);font-weight:400;font-size:11.4px;line-height:14.8px;margin-top:3px;width:405px}

.footer-band{position:absolute;left:0;top:1080px;width:969px;height:120px}
.contact{position:absolute;left:46px;top:1116px;color:var(--white)}
.contact .phone{display:flex;align-items:center;gap:10px;font-weight:800;font-size:36px;line-height:40px}
.contact .email{display:flex;align-items:center;gap:12px;font-weight:400;font-size:19px;line-height:26px;margin-top:2px}
.website{position:absolute;left:527px;top:1152px;color:var(--navy);font-weight:700;font-size:26px}
</style>
</head>
<body>
<div class="flyer">
  <div class="hero-photo" role="img" aria-label="Photo of a businessman in a dark suit tapping a tablet, surrounded by glowing technology icons over a city skyline"></div>

  <svg class="hero-shapes" viewBox="0 0 969 580" aria-hidden="true">
    <path d="M490 478 H969 V530 H600 Z" fill="#0c0d10"/>
    <path d="M512 515 Q520 506 540 506 H890 L870 560 H500 Q505 535 512 515 Z" fill="var(--navy)"/>
    <path d="M880 506 H928 L905 560 H858 Z" fill="var(--red)"/>
    <path d="M862 506 H884 L862 560 H842 Z" fill="#e07a6a"/>
    <path d="M560 527 H969 V580 H520 Z" fill="var(--white)"/>
    <path d="M0 358 H382 Q400 358 412 375 L490 484 Q500 500 485 515 L470 530 Q455 542 430 542 H0 Z" fill="var(--white)"/>
    <path d="M0 542 H430 Q455 542 470 530 L485 515 Q500 500 490 484" fill="none" stroke="var(--rule)" stroke-width="1.3"/>
  </svg>

  <div class="brand">
    <div class="brand-mark"></div>
    <div class="brand-name">GEAR BY MARLON</div>
  </div>

  <div class="services-pill">Our Services</div>

  <h1 class="why-title">Why Choose Gear By Marlon?</h1>

  <h2 class="why-head" style="top:655px;width:330px">Personalized Solutions and Support</h2>
  <p class="why-text" style="top:722px">We know your time is valuable and your technology is critical. That's why we take time to visit with each of our clients and recommend the best solution for them. Your not just another client to us, we want what is best for you.</p>

  <h2 class="why-head" style="top:814px">Experience</h2>
  <p class="why-text" style="top:853px">We have years of experience in both large and small environments. We know what solutions are available and how to implement them in your business. We are constantly working with industry experts with today's changing technology.</p>

  <h2 class="why-head" style="top:952px">One Stop Shop</h2>
  <p class="why-text" style="top:990px">We can help you with all your IT needs, weather it be computer or network security. Phone and Voice needs, or cloud services. Contact us today to discuss how we can help you.</p>

  <div class="divider"></div>

  <p class="offer">We provide a complete range of IT services focused on you getting the most from your technology.</p>

  <div class="service" style="top:640px">
    <div class="service-icon" style="margin-top:-3px"><svg viewBox="0 0 36 36" fill="none" stroke="#fff" stroke-width="2"><rect x="5" y="5" width="26" height="20" rx="2"/><path d="M12 25 L10 31 L17 25"/><path d="M11 10 L25 21 M25 10 L11 21"/></svg></div>
    <div><h3>MANAGED IT SERVICES</h3><p>You need your IT systems for your day to day work. Let us help manage and protect them.</p></div>
  </div>

  <div class="service" style="top:714px">
    <div class="service-icon" style="margin-top:-1px"><svg viewBox="0 0 36 36" fill="#fff"><path d="M8 10 c2-2 4-2 5 0 l2 4 c1 2 0 3-1 4 c1 3 3 5 6 6 c1-1 2-2 4-1 l4 2 c2 1 2 3 0 5 c-3 3-9 2-15-4 s-7-12-5-16z"/><rect x="18" y="3" width="14" height="10" rx="2"/><path d="M21 13 l-1 4 4-4z"/><circle cx="22" cy="8" r="1" fill="var(--red)"/><circle cx="25" cy="8" r="1" fill="var(--red)"/><circle cx="28" cy="8" r="1" fill="var(--red)"/></svg></div>
    <div><h3>Business VOIP</h3><p>Reduce cost and improve communication for your business. Solutions available for any size business from 1 phone to hundreds of phones.</p></div>
  </div>

  <div class="service" style="top:792px">
    <div class="service-icon"><svg viewBox="0 0 36 36" fill="#fff"><path d="M12 15 v-4 a6 6 0 0 1 12 0 v4" fill="none" stroke="#fff" stroke-width="2.4"/><rect x="8" y="15" width="20" height="15" rx="2"/><circle cx="18" cy="21" r="2" fill="var(--red)"/><rect x="17" y="21" width="2" height="5" fill="var(--red)"/></svg></div>
    <div><h3>SECURITY &amp; SURVEILLANCE</h3><p>Through our partner Blue Pine Safety we offer camera, alarm and access control systems to protect your office.</p></div>
  </div>

  <div class="service" style="top:871px">
    <div class="service-icon" style="margin-top:5px"><svg viewBox="0 0 36 36" fill="#fff"><rect x="3" y="5" width="22" height="6" rx="2"/><rect x="3" y="13" width="18" height="6" rx="2"/><rect x="3" y="21" width="16" height="6" rx="2"/><path d="M26 15 l7 3 v5 c0 5-4 8-7 9 c-3-1-7-4-7-9 v-5z"/><path d="M23 23 l2.5 2.5 l4.5-5" stroke="var(--red)" stroke-width="2" fill="none"/></svg></div>
    <div><h3>NETWORK SECURITY</h3><p>Worried about the latest ransomware or crypto virus? We can help design and protect your network.</p></div>
  </div>

  <div class="service" style="top:958px">
    <div class="service-icon" style="margin-top:-5px"><svg viewBox="0 0 36 36" fill="none" stroke="#fff" stroke-width="2"><rect x="4" y="21" width="28" height="9" rx="2"/><path d="M10 21 L7 14 M26 21 L29 14"/><path d="M12 12 a8 8 0 0 1 12 0 M14.5 15 a4.5 4.5 0 0 1 7 0"/><circle cx="18" cy="18" r="1" fill="#fff"/><path d="M22 25.5 h2 M25.5 25.5 h2"/></svg></div>
    <div><h3>WIRELESS SOLUTIONS</h3><p>Is your wireless coverage spotty or would you like to extend your network or internet coverage to another building?</p></div>
  </div>

  <div class="service" style="top:1031px">
    <div class="service-icon" style="margin-top:6px"><svg viewBox="0 0 36 36" fill="none" stroke="#fff" stroke-width="2"><path d="M9 21 a5 5 0 0 1 1-10 a8 8 0 0 1 15 1 a4.5 4.5 0 0 1 1 9 z"/><path d="M13 21 v5 M18 21 v8 M23 21 v5"/><circle cx="13" cy="28" r="2"/><circle cx="18" cy="31" r="2"/><circle cx="23" cy="28" r="2"/></svg></div>
    <div><h3>CLOUD SERVICES</h3><p>Want your own business email service? Want to move to the cloud for secure file storage and sharing? Ask us about our complete cloud solution services.</p></div>
  </div>

  <svg class="footer-band" viewBox="0 0 969 120" aria-hidden="true">
    <path d="M0 0 H330 Q350 0 362 14 L444 120 H0 Z" fill="var(--red-deep)"/>
    <path d="M0 24 H330 Q340 24 348 34 L418 120" fill="none" stroke="rgba(255,255,255,.55)" stroke-width="1.3"/>
    <path d="M421 120 L448 76 Q456 64 470 64 H969" fill="none" stroke="var(--rule)" stroke-width="1.3"/>
  </svg>

  <div class="contact">
    <div class="phone"><svg width="28" height="28" viewBox="0 0 28 28" fill="none" stroke="#fff" stroke-width="2"><circle cx="14" cy="14" r="12"/><path d="M9 8 c1-1 2-1 3 0 l1 2 c0 1 0 2-1 2 c1 2 2 3 4 4 c0-1 1-1 2-1 l2 1 c1 1 1 2 0 3 c-2 2-5 1-8-2 s-4-7-3-9z" fill="#fff" stroke="none"/></svg>320.555.0147</div>
    <div class="email"><svg width="22" height="16" viewBox="0 0 22 16"><rect width="22" height="16" rx="2" fill="#fff"/><path d="M1 2 L11 9 L21 2" stroke="var(--red-deep)" stroke-width="2" fill="none"/></svg>sales@gearbymarlon.com</div>
  </div>

  <div class="website">www.gearbymarlon.com</div>
</div>
</body>
</html>
```